Stonebay Towing Business Card

Towing
Accident towing
Mechanical breakdown
Insurance, salvage and recovery
4wd off road towing
Light & Heavy towing
8347 2516
24 hour business 7 days

Logo can be whole size on front

Industry/Entity Type

Towing/ transport

Contact Information for Business Card

The above

```html
<!DOCTYPE html>
<html lang="en">
<head>
<meta charset="utf-8">
<title>Stonebay Towing Business Card</title>
<link rel="stylesheet" href="https://fonts.googleapis.com/css2?family=Montserrat:wght@400;500;700;800&display=swap">
<style>
  :root {
    --backdrop: #b1b1b1;
    --card: #ffffff;
    --brand-red: #d21f26;
    --ink: #111111;
    --black: #000000;
  }
  * { margin: 0; padding: 0; box-sizing: border-box; }
  html, body { width: 1200px; height: 716px; overflow: hidden; }
  body {
    background: var(--backdrop);
    font-family: "Montserrat", Arial, sans-serif;
    color: var(--ink);
    position: relative;
  }
  .card {
    position: absolute;
    left: 369px;
    width: 461px;
    height: 264px;
    background: var(--card);
    overflow: hidden;
  }
  .card-front { top: 94px; }
  .card-back { top: 385px; }

  .brand-name {
    position: absolute;
    left: 0; right: 0;
    text-align: center;
    font-weight: 800;
    color: var(--brand-red);
    white-space: nowrap;
    letter-spacing: -0.5px;
  }
  .card-front .brand-name { top: 106px; font-size: 38px; }
  .card-back .brand-name { top: 36px; font-size: 22px; }

  .services {
    position: absolute;
    top: 111px;
    left: 0; right: 0;
    display: flex;
    flex-direction: column;
    align-items: center;
    gap: 5px;
  }
  .service-row { display: flex; gap: 12px; }
  .service {
    display: flex;
    align-items: center;
    gap: 6px;
    font-size: 11.5px;
    font-weight: 500;
    line-height: 14px;
    white-space: nowrap;
  }
  .tick { width: 12px; height: 12px; flex: none; }

  .phone {
    position: absolute;
    top: 177px;
    left: 0; right: 0;
    display: flex;
    justify-content: center;
    align-items: center;
    gap: 8px;
    font-size: 31px;
    font-weight: 700;
    letter-spacing: -0.5px;
    line-height: 1;
  }
  .phone-icon { width: 34px; height: 26px; }
  .hours {
    position: absolute;
    top: 211px;
    left: 0; right: 0;
    text-align: center;
    font-size: 11px;
    font-weight: 700;
    letter-spacing: 2.6px;
  }
  .footer-band {
    position: absolute;
    left: 0; bottom: 0;
    width: 461px; height: 28px;
  }
</style>
</head>
<body>
  <section class="card card-front" aria-label="Card front">
    <h1 class="brand-name">Stonebay Towing</h1>
  </section>

  <section class="card card-back" aria-label="Card back">
    <p class="brand-name">Stonebay Towing</p>

    <ul class="services">
      <li class="service-row">
        <span class="service"><svg class="tick" viewBox="0 0 12 12"><circle cx="6" cy="6" r="6" fill="var(--brand-red)"/><path d="M3.3 6.2 5.2 8 8.8 4.2" fill="none" stroke="#fff" stroke-width="1.6" stroke-linecap="round" stroke-linejoin="round"/></svg>Towing</span>
        <span class="service"><svg class="tick" viewBox="0 0 12 12"><circle cx="6" cy="6" r="6" fill="var(--brand-red)"/><path d="M3.3 6.2 5.2 8 8.8 4.2" fill="none" stroke="#fff" stroke-width="1.6" stroke-linecap="round" stroke-linejoin="round"/></svg>Accident Towing</span>
        <span class="service"><svg class="tick" viewBox="0 0 12 12"><circle cx="6" cy="6" r="6" fill="var(--brand-red)"/><path d="M3.3 6.2 5.2 8 8.8 4.2" fill="none" stroke="#fff" stroke-width="1.6" stroke-linecap="round" stroke-linejoin="round"/></svg>Mechanical Breakdown</span>
      </li>
      <li class="service-row">
        <span class="service"><svg class="tick" viewBox="0 0 12 12"><circle cx="6" cy="6" r="6" fill="var(--brand-red)"/><path d="M3.3 6.2 5.2 8 8.8 4.2" fill="none" stroke="#fff" stroke-width="1.6" stroke-linecap="round" stroke-linejoin="round"/></svg>Insurance, Salvage and Recovery</span>
        <span class="service"><svg class="tick" viewBox="0 0 12 12"><circle cx="6" cy="6" r="6" fill="var(--brand-red)"/><path d="M3.3 6.2 5.2 8 8.8 4.2" fill="none" stroke="#fff" stroke-width="1.6" stroke-linecap="round" stroke-linejoin="round"/></svg>4wd off Road Towing</span>
      </li>
      <li class="service-row">
        <span class="service"><svg class="tick" viewBox="0 0 12 12"><circle cx="6" cy="6" r="6" fill="var(--brand-red)"/><path d="M3.3 6.2 5.2 8 8.8 4.2" fill="none" stroke="#fff" stroke-width="1.6" stroke-linecap="round" stroke-linejoin="round"/></svg>Light &amp; Heavy towing</span>
      </li>
    </ul>

    <p class="phone">
      <svg class="phone-icon" viewBox="0 0 34 26" aria-hidden="true">
        <path d="M1 8 C1 2 33 2 33 8 L33 10 L25 10 L25 7 L9 7 L9 10 L1 10 Z" fill="var(--brand-red)"/>
        <path d="M10 9 L24 9 L29 25 L5 25 Z" fill="var(--brand-red)"/>
        <g fill="#fff">
          <rect x="13" y="13" width="2" height="2"/><rect x="16" y="13" width="2" height="2"/><rect x="19" y="13" width="2" height="2"/>
          <rect x="13" y="16" width="2" height="2"/><rect x="16" y="16" width="2" height="2"/><rect x="19" y="16" width="2" height="2"/>
          <rect x="13" y="19" width="2" height="2"/><rect x="16" y="19" width="2" height="2"/><rect x="19" y="19" width="2" height="2"/>
        </g>
      </svg>
      <span>8347 2516</span>
    </p>
    <p class="hours">24 Hour Business 7 Days</p>

    <svg class="footer-band" viewBox="0 0 461 28" aria-hidden="true">
      <rect x="0" y="14" width="461" height="14" fill="var(--black)"/>
      <path d="M107 28 C125 -4 138 0 172 0 L290 0 C324 0 337 -4 355 28 Z" fill="#fff"/>
      <path d="M112 28 C128 2 140 0 172 0 L290 0 C322 0 334 2 350 28 Z" fill="var(--brand-red)"/>
    </svg>
  </section>
</body>
</html>
```